Homvuk Business Card Project showing the logo and a bellan image on the rear

Design a whacky but professional business card, the logo is for the front and the Bellan image is for the rear. Happy to consider other open source Bellan Images if the designer wants to select one from the web. Homvuk is a competitor to TKU.com.au and Parcelo.com.au and is based around every property in Australia

Target Market(s)

Business

Contact Information for Business Card

Name, Title, Email, Web, Phone Number

Font styles to use
Other font styles liked:
• avenir

Requirements
Must have
• Image on Back logo on front
Nice to have
• Happy to consider other images on rear, preftably Oskar Bellan. Image supplied I own, we can use open source other Bellan Images

```html
<!DOCTYPE html>
<html lang="en">
<head>
<meta charset="UTF-8">
<title>Homvuk Business Card</title>
<link rel="stylesheet" href="https://fonts.googleapis.com/css2?family=Nunito+Sans:wght@400;700;800&display=swap">
<style>
  :root {
    --bg: #2a2a2b;
    --card-white: #ffffff;
    --ink: #111111;
    --orange: #f39420;
    --art-green: #3f6b2e;
    --art-orange: #e8692a;
    --art-red: #d9402a;
    --art-olive: #5a4d22;
  }
  * { margin: 0; padding: 0; box-sizing: border-box; }
  html, body {
    width: 1200px; height: 900px; overflow: hidden;
    background: var(--bg);
    font-family: "Nunito Sans", Arial, sans-serif;
  }
  .canvas { position: relative; width: 1200px; height: 900px; }

  .card {
    position: absolute; left: 240px; width: 720px; height: 410px;
    border-radius: 22px; overflow: hidden;
    box-shadow: 0 12px 30px rgba(0,0,0,0.45);
  }

  /* Rear side */
  .card-back { top: 28px; }
  .card-back .artwork {
    position: absolute; inset: 0;
    background:
      linear-gradient(180deg, rgba(63,107,46,0.9) 0%, rgba(63,107,46,0) 40%),
      linear-gradient(100deg, var(--art-olive) 0%, var(--art-orange) 35%, var(--art-red) 55%, var(--art-orange) 75%, var(--art-green) 100%);
  }
  .card-back .brand {
    position: absolute; right: 50px; bottom: 52px;
    display: flex; align-items: center; gap: 16px;
  }
  .card-back .brand-mark { width: 54px; height: 54px; background: var(--orange); }
  .card-back .brand-name {
    font-size: 64px; font-weight: 800; color: var(--card-white); letter-spacing: 1px;
  }

  /* Front side */
  .card-front { top: 462px; background: var(--card-white); }
  .card-front .brand {
    position: absolute; left: 52px; top: 48px;
    display: flex; align-items: center; gap: 20px;
  }
  .card-front .brand-mark { width: 72px; height: 72px; background: var(--orange); }
  .card-front .brand-name {
    font-size: 72px; font-weight: 800; color: var(--ink); letter-spacing: 1px;
  }
  .divider {
    position: absolute; left: 60px; right: 60px; top: 212px;
    height: 1.5px; background: var(--ink);
  }
  .contact-list {
    position: absolute; left: 48px; top: 236px; list-style: none;
    font-size: 20px; color: var(--ink); line-height: 1.5;
  }
  .contact-list li { display: flex; align-items: center; gap: 10px; }
  .contact-list svg { width: 20px; height: 20px; flex: none; }

  .person { position: absolute; right: 58px; top: 232px; text-align: right; }
  .person-name {
    font-size: 30px; font-weight: 800; color: var(--orange); letter-spacing: 1.5px;
  }
  .person-title { font-size: 21px; color: var(--ink); letter-spacing: 1px; }
  .person-rule { height: 1.5px; background: var(--ink); margin-top: 8px; }
  .address {
    position: absolute; right: 58px; top: 332px; text-align: right;
    font-size: 21px; color: var(--ink); line-height: 1.25; letter-spacing: 0.5px;
  }
  .accent-band { position: absolute; left: 0; bottom: 0; width: 720px; height: 16px; }
</style>
</head>
<body>
<div class="canvas">

  <section class="card card-back">
    <div class="artwork" role="img" aria-label="Colourful naive-style city illustration of tall buildings, clouds, sun and stars in orange, red and green"></div>
    <div class="brand">
      <span class="brand-mark"></span>
      <span class="brand-name">Homvuk</span>
    </div>
  </section>

  <section class="card card-front">
    <div class="brand">
      <span class="brand-mark"></span>
      <span class="brand-name">Homvuk</span>
    </div>

    <div class="divider"></div>

    <ul class="contact-list">
      <li>
        <svg viewBox="0 0 20 20" aria-hidden="true"><circle cx="10" cy="10" r="10" fill="#f39420"/><path d="M7 5.5l1.6 2.4-1 1a6 6 0 0 0 3.5 3.5l1-1 2.4 1.6-1 1.6c-3.6 0-7.1-3.5-7.1-7.1z" fill="#fff"/></svg>
        415-286-7192
      </li>
      <li>
        <svg viewBox="0 0 20 20" aria-hidden="true"><circle cx="10" cy="10" r="10" fill="#f39420"/><rect x="5" y="6.5" width="10" height="7" fill="none" stroke="#fff" stroke-width="1.3"/><path d="M5 6.5l5 4 5-4" fill="none" stroke="#fff" stroke-width="1.3"/></svg>
        Tomas@homvuk.com.au
      </li>
      <li>
        <svg viewBox="0 0 20 20" aria-hidden="true"><circle cx="10" cy="10" r="10" fill="#f39420"/><circle cx="10" cy="10" r="5" fill="none" stroke="#fff" stroke-width="1.3"/><path d="M5 10h10M10 5c-2.5 3-2.5 7 0 10M10 5c2.5 3 2.5 7 0 10" fill="none" stroke="#fff" stroke-width="1"/></svg>
        www.homvuk.com.au
      </li>
    </ul>

    <div class="person">
      <div class="person-name">TOMAS WRENFIELD</div>
      <div class="person-title">Executive Producer</div>
      <div class="person-rule"></div>
    </div>

    <div class="address">
      1480 Harlow Avenue<br>
      Westmere County name 6184
    </div>

    <svg class="accent-band" viewBox="0 0 720 16" preserveAspectRatio="none" aria-hidden="true">
      <polygon points="0,0 300,0 288,16 0,16" fill="#111111"/>
      <polygon points="300,0 720,0 720,16 288,16" fill="#f39420"/>
    </svg>
  </section>

</div>
</body>
</html>
```